Law Firm Website Update

I have an existing website but it is very wordy, not very aesthetically pleasing and I want additional features. I would like to update the areas of law and pictures, I would like to add a page for a client to fill in their information and links to other pages. Also want to make it more mobile friendly. site is www.brightmerelegal.com

Coding

Coded - Design and coding required

```html
<!DOCTYPE html>
<html lang="en">
<head>
<meta charset="utf-8">
<title>Brightmere Legal — Northern California Legal Guidance</title>
<link href="https://fonts.googleapis.com/css2?family=Cinzel:wght@400;600;700&family=Poppins:wght@400;500;600&display=swap" rel="stylesheet">
<style>
:root{
  --red:#d42027;
  --red-dark:#b3161c;
  --ink:#1d1d1f;
  --text:#4a4a4f;
  --muted:#8a8a92;
  --pale:#eef0f4;
  --line:#e2e4e8;
  --black:#0d0d0d;
  --white:#ffffff;
  --serif:"Cinzel", serif;
  --sans:"Poppins", sans-serif;
}
*{box-sizing:border-box;margin:0;padding:0}
html,body{width:1200px;height:4272px;overflow:hidden;background:var(--white)}
body{position:relative;font-family:var(--sans);color:var(--text)}
.abs{position:absolute}

/* header */
.site-header{position:absolute;left:0;top:0;width:1200px;height:112px;background:var(--white);z-index:5}
.brand{position:absolute;left:112px;top:22px;font-family:var(--serif);font-weight:700;font-size:34px;color:var(--red);letter-spacing:.5px}
.brand-tag{position:absolute;left:112px;top:66px;font-size:11px;letter-spacing:3px;color:var(--muted)}
.topline{position:absolute;right:112px;top:10px;font-size:12px;color:var(--text);display:flex;gap:24px}
.topline b{color:var(--red);font-weight:600}
.topline-rule{position:absolute;left:400px;right:0;top:36px;height:1px;background:var(--line)}
.main-nav{position:absolute;left:400px;top:58px;display:flex;gap:36px;font-size:13px;font-weight:500;color:var(--ink);text-transform:uppercase}
.main-nav .active{color:var(--red);border-bottom:2px solid var(--red);padding-bottom:6px}
.btn{display:inline-block;background:var(--red);color:var(--white);font-family:var(--sans);font-weight:600;font-size:13px;text-transform:uppercase;padding:14px 26px;letter-spacing:.5px}
.nav-cta{position:absolute;right:88px;top:46px}

/* hero */
.hero{position:absolute;left:0;top:112px;width:1200px;height:800px;background:linear-gradient(180deg,#3c352f 0%,#5b5148 45%,#2a2521 100%)}
.hero-cut{position:absolute;left:0;top:800px;width:1200px;height:120px}
.play{position:absolute;left:560px;top:340px;width:80px;height:80px;border-radius:50%;background:var(--red)}
.hero h1{position:absolute;left:0;width:1200px;top:572px;text-align:center;font-family:var(--serif);font-weight:700;font-size:56px;color:var(--white);letter-spacing:2px}
.hero .sub{position:absolute;left:0;width:1200px;top:654px;text-align:center;font-family:var(--serif);font-size:22px;color:var(--white);letter-spacing:2px}

/* section titles */
.section-title{position:absolute;left:0;width:1200px;text-align:center;font-family:var(--serif);font-weight:600;font-size:44px;color:var(--ink);letter-spacing:1px}
.section-title em{font-style:normal;color:var(--red)}

/* awards */
.badge{position:absolute;top:1046px;width:190px;height:92px;background:var(--pale);border-radius:6px}

/* about */
.about{position:absolute;left:0;top:1190px;width:1200px;height:620px;background:var(--pale)}
.about-frame{position:absolute;left:84px;top:1244px;width:380px;height:420px;border:6px solid var(--red)}
.about-photo{position:absolute;left:108px;top:1268px;width:432px;height:456px;background:linear-gradient(160deg,#d8d2c8,#8d8478 60%,#4a4640)}
.about-copy{position:absolute;left:600px;top:1296px;width:500px}
.about-copy h2{font-family:var(--serif);font-weight:700;font-size:34px;line-height:1.15;color:var(--ink);border-left:5px solid var(--red);padding-left:14px}
.about-copy h3{font-family:var(--serif);font-size:17px;font-weight:600;color:var(--red);margin:10px 0 22px 19px}
.about-copy p{font-size:14px;line-height:1.75;color:var(--text)}
.about-copy .btn{margin-top:24px}

/* practice */
.practice-bg{position:absolute;left:0;top:1880px;width:1200px;height:440px}
.tile{position:absolute;top:1968px;width:192px;height:212px;background:linear-gradient(180deg,#4a4a50,#151517)}
.tile span{position:absolute;left:0;right:0;bottom:28px;text-align:center;font-family:var(--serif);font-weight:600;font-size:16px;color:var(--white);line-height:1.2}
.view-all{position:absolute;left:540px;top:2220px}

/* attorney */
.attorney{position:absolute;left:0;top:2350px;width:1200px;height:480px}
.attorney-frame{position:absolute;left:200px;top:2440px;width:340px;height:360px;border:3px solid var(--white)}
.attorney-photo{position:absolute;left:180px;top:2460px;width:340px;height:360px;background:linear-gradient(170deg,#e7e3df,#b8aea6 55%,#2b2626)}
.attorney-copy{position:absolute;left:660px;top:2520px;width:440px;color:var(--white)}
.attorney-copy h2{font-family:var(--serif);font-weight:700;font-size:38px;line-height:1.15}
.attorney-copy p{font-size:14px;line-height:1.7;margin:14px 0 22px}
.btn-light{background:var(--white);color:var(--red)}

/* reviews */
.review{position:absolute;top:3008px;width:320px;height:312px;background:var(--white);box-shadow:0 6px 24px rgba(0,0,0,.12);padding:24px}
.review .avatar{position:absolute;left:24px;top:24px;width:40px;height:40px;border-radius:50%;background:#d9d9de}
.review .who{margin-left:52px;font-size:13px;font-weight:600;color:var(--ink)}
.review .stars{margin-left:52px;font-size:14px;color:#f5b400;letter-spacing:1px}
.review .stars small{color:var(--text);font-size:12px;margin-left:6px}
.review p{margin-top:28px;font-size:13px;line-height:1.7;color:var(--text)}
.review .role{margin-top:14px;font-family:var(--serif);font-weight:700;font-size:14px;color:var(--ink)}
.arrow{position:absolute;top:3140px;width:34px;height:34px;border-radius:50%;background:var(--white);box-shadow:0 2px 8px rgba(0,0,0,.15)}
.dots{position:absolute;left:0;width:1200px;top:3400px;display:flex;justify-content:center;gap:12px}
.dots i{width:12px;height:12px;border-radius:50%;background:#d6d6dc}
.dots i.on{background:var(--red)}

/* contact */
.map{position:absolute;left:0;top:3430px;width:1200px;height:500px;background:linear-gradient(135deg,#e8ebee,#d7dde2 50%,#e3e7ea)}
.contact-card{position:absolute;left:620px;top:3460px;width:460px;height:440px;background:var(--white);box-shadow:0 8px 30px rgba(0,0,0,.15);padding:32px 36px}
.contact-card h2{font-family:var(--serif);font-weight:600;font-size:40px;color:var(--ink)}
.contact-card h2 em{font-style:normal;color:var(--red)}
.contact-card .intro{font-size:14px;line-height:1.5;margin:6px 0 16px}
.field-grid{display:grid;grid-template-columns:1fr 1fr;gap:14px 18px}
.field label{display:block;font-size:11px;color:var(--ink);font-weight:500;margin-bottom:4px}
.field div{height:32px;border:1px solid var(--line);font-size:11px;color:var(--muted);padding:8px 10px}
.field.wide{grid-column:1 / 3}
.field.wide div{height:54px}
.contact-card .btn{margin-top:16px;padding:11px 24px}

/* footer */
.site-footer{position:absolute;left:0;top:3940px;width:1200px;height:332px;background:var(--black);color:#c9c9cc}
.f-brand{position:absolute;left:112px;top:40px;font-family:var(--serif);font-weight:700;font-size:32px;color:var(--red)}
.f-about{position:absolute;left:112px;top:92px;width:300px;font-size:13px;line-height:1.7}
.f-free{position:absolute;left:112px;top:176px;font-family:var(--serif);font-weight:600;font-size:15px;color:var(--white)}
.socials{position:absolute;left:112px;top:210px;display:flex;gap:10px}
.socials i{width:30px;height:30px;border-radius:50%;background:var(--red)}
.f-col{position:absolute;top:44px}
.f-col h4{font-family:var(--serif);font-weight:700;font-size:16px;color:var(--white);border-left:3px solid var(--red);padding-left:10px;margin-bottom:18px}
.f-col li{list-style:none;font-size:13px;line-height:2}
.f-col .sub-box{display:flex;margin-top:14px}
.f-col .sub-box div{width:190px;height:36px;background:var(--white);font-size:11px;color:var(--muted);padding:10px}
.f-col .sub-box span{width:36px;height:36px;background:var(--red)}
.f-bottom{position:absolute;left:112px;right:112px;bottom:0;height:50px;border-top:1px solid #2a2a2a;display:flex;justify-content:space-between;align-items:center;font-size:12px;color:#8e8e94}
</style>
</head>
<body>

<header class="site-header">
  <div class="brand">Brightmere Legal</div>
  <div class="brand-tag">ATTORNEYS AT LAW</div>
  <div class="topline">
    <span><b>Our Location:</b> 1420 Alder Grove Road, Suite B, Chico, California 95926</span>
    <span><b>☎</b> 530-555-0148</span>
    <span><b>✆</b> 530-555-0149</span>
  </div>
  <div class="topline-rule"></div>
  <nav class="main-nav">
    <span class="active">Home</span><span>About Us</span><span>Attorney Profile</span><span>Practice Areas ▾</span><span>Reviews</span><span>Payments</span>
  </nav>
  <span class="btn nav-cta">Contact Us</span>
</header>

<section class="hero" role="img" aria-label="Courthouse columns photo, dark and warm toned">
  <div class="play"></div>
  <svg class="abs" style="left:592px;top:366px" width="22" height="28" viewBox="0 0 22 28"><path d="M0 0 L22 14 L0 28 Z" fill="#fff"/></svg>
  <h1>NORTHERN CALIFORNIA</h1>
  <div class="sub">LEGAL GUIDANCE FOR INDIVIDUALS &amp; BUSINESSES</div>
</section>
<svg class="hero-cut" viewBox="0 0 1200 120" preserveAspectRatio="none"><path d="M0 20 L600 120 L1200 20 L1200 120 L0 120 Z" fill="#fff"/><path d="M0 20 L600 110 L1200 20" fill="none" stroke="#d42027" stroke-width="3"/></svg>

<h2 class="section-title" style="top:950px">AWARDS &amp; MEMBERSHIPS</h2>
<div class="badge" style="left:90px"></div>
<div class="badge" style="left:297px"></div>
<div class="badge" style="left:505px"></div>
<div class="badge" style="left:713px"></div>
<div class="badge" style="left:920px"></div>

<section class="about"></section>
<div class="about-frame"></div>
<div class="about-photo" role="img" aria-label="Attorney in a suit reading a law book"></div>
<div class="about-copy">
  <h2>EXPERIENCED<br>CALIFORNIA ATTORNEY</h2>
  <h3>ASSISTS WITH A WIDE RANGE OF LEGAL MATTERS</h3>
  <p>Legal issues related to property and finances can be hard to resolve on your own. Instead of trying to tread the line between handling simple issues and determining when to get advice, talk to an experienced attorney about your legal options. At Brightmere Legal, we assist clients throughout the North Sacramento Valley with real estate transactions, business concerns, bankruptcy filing, litigation and other related matters. Whether you need a sale contract reviewed, a business formation plan created, debt analysis or information about pursuing legal action, our attorney will provide you with sound advice.</p>
  <span class="btn">Read More</span>
</div>

<svg class="practice-bg" viewBox="0 0 1200 440" preserveAspectRatio="none"><path d="M0 260 L300 140 L620 300 L900 160 L1200 280 L1200 440 L0 440 Z" fill="#f3f4f7"/></svg>
<h2 class="section-title" style="top:1900px">PRACTICE <em>AREAS</em></h2>
<div class="tile" style="left:90px" role="img" aria-label="City buildings photo"><span>REAL ESTATE</span></div>
<div class="tile" style="left:297px" role="img" aria-label="Scales of justice photo"><span>BUSINESS LAW</span></div>
<div class="tile" style="left:504px" role="img" aria-label="Bankruptcy paperwork photo"><span>BANKRUPTCY</span></div>
<div class="tile" style="left:711px" role="img" aria-label="Meeting handshake photo"><span>DISPUTE<br>RESOLUTION</span></div>
<div class="tile" style="left:918px" role="img" aria-label="Estate documents photo"><span>ESTATE PLANNING</span></div>
<span class="btn view-all">View All</span>

<svg class="attorney" viewBox="0 0 1200 480" preserveAspectRatio="none"><path d="M0 60 L1200 0 L1200 420 L0 480 Z" fill="#d42027"/></svg>
<div class="attorney-frame"></div>
<div class="attorney-photo" role="img" aria-label="Portrait of the lead attorney"></div>
<div class="attorney-copy">
  <h2>DANA M. WHITLOCK<br>ATTORNEY</h2>
  <p>Dana Whitlock is a California real estate attorney and principal of Brightmere Legal, specializing in corporate law, business law, and property matters.</p>
  <span class="btn btn-light">View Bio</span>
</div>

<h2 class="section-title" style="top:2930px"><em>REVIEWS</em> &amp; RATINGS</h2>
<div class="arrow" style="left:62px"></div>
<div class="arrow" style="left:1104px"></div>
<div class="review" style="left:100px">
  <div class="avatar"></div>
  <div class="who">MARISOL T.</div>
  <div class="stars">★★★★★<small>5.0/5.0</small></div>
  <p>As long as you have Dana in your corner, justice and fairness are still alive. The plaintiffs against me with their egregious and slanderous claims tried to cripple my freedoms...</p>
  <div class="role">CLIENT</div>
</div>
<div class="review" style="left:440px">
  <div class="avatar"></div>
  <div class="who">GREGORY H.</div>
  <div class="stars">★★★★★<small>5.0/5.0</small></div>
  <p>I really enjoyed working with Dana, she assisted us in our corporation set up, as well as some real estate transactions. She is professional and excellent at what she does...</p>
  <div class="role">CLIENT</div>
</div>
<div class="review" style="left:780px">
  <div class="avatar"></div>
  <div class="who">LEANNE R.</div>
  <div class="stars">★★★★★<small>5.0/5.0</small></div>
  <p>A very smart attorney I want always on my corner. She is down to earth and very real with you. She can think outside the box which is why she is so good. She was a great help to my uncle...</p>
  <div class="role">CLIENT</div>
</div>
<div class="dots"><i></i><i></i><i class="on"></i><i></i><i></i></div>

<div class="map" role="img" aria-label="Street map of Chico with the office location marked"></div>
<svg class="abs" style="left:250px;top:3580px" width="36" height="48" viewBox="0 0 36 48"><path d="M18 0 C8 0 0 8 0 18 C0 31 18 48 18 48 C18 48 36 31 36 18 C36 8 28 0 18 0 Z" fill="#d42027"/><circle cx="18" cy="18" r="7" fill="#fff"/></svg>
<div class="contact-card">
  <h2>CONTACT <em>US</em></h2>
  <p class="intro">Please fill out the form below and one of our attorneys will contact you.</p>
  <div class="field-grid">
    <div class="field"><label>First Name</label><div>Your first name</div></div>
    <div class="field"><label>Last Name</label><div>Your last name</div></div>
    <div class="field"><label>Email Address</label><div>Your email</div></div>
    <div class="field"><label>Phone</label><div>Phone number</div></div>
    <div class="field wide"><label>Message</label><div>How can we help you?</div></div>
  </div>
  <span class="btn">Submit</span>
</div>

<footer class="site-footer">
  <div class="f-brand">Brightmere Legal</div>
  <p class="f-about">Brightmere Legal is located in Chico, CA and serves clients in and around Chico, Durham, Paradise and Butte.</p>
  <div class="f-free">FREE CONSULTATION</div>
  <div class="socials"><i></i><i></i><i></i><i></i></div>
  <div class="f-col" style="left:470px">
    <h4>QUICK LINKS</h4>
    <ul><li>Home</li><li>About Us</li><li>Attorney Profile</li><li>Practice Areas</li><li>Reviews</li><li>Payments</li></ul>
  </div>
  <div class="f-col" style="left:640px">
    <h4>CONTACT US</h4>
    <ul><li>☎ 530-555-0148</li><li>✆ 530-555-0149</li><li>1420 Alder Grove Road, Suite B,</li><li>Chico, California 95926</li></ul>
  </div>
  <div class="f-col" style="left:860px">
    <h4>SUBSCRIBE NEWSLETTER</h4>
    <p style="font-size:13px;line-height:1.6">Subscribe our newsletter for the latest offers and news.</p>
    <div class="sub-box"><div>Your email</div><span></span></div>
  </div>
  <div class="f-bottom"><span>Copyright © 2024 Brightmere Legal. All rights reserved.</span><span>Privacy Policy | Terms &amp; Conditions</span></div>
</footer>

</body>
</html>
```